Kitchen and cabinet shop needs new website

Benvoe Cabinets is a mid-sized, family run cabinet shop that is in the process of updating it's image after being handed over to the second generation. It's been in the business for almost 30 years and our designers have lots of experience in the design, home building and renovation industry. Our business offers free home consultations or a customer can visit our showroom to start the design process. Whether the client is a designer, home builder or homeowner we can help create the kitchen and space you're after by helping every step of the way.

The website needs to showcase our past work, (pictures to be included), show the different styles (eg. traditional, modern) and different areas of the home we can produce cabinets for. We created a new logo with Sketch hive that needs to be included in the website as well as the colours. I would like 5 pages;
-Home page
-About us
-portfolio/gallery
-services
-contact us

I would like the website to have a contemporary look, nothing too busy or complicated.

I will attach some pictures with the different styles of our work I mentioned above and provide content for each job.
Updates

Target Market(s)

home owners, designer, home builders, business owners

Industry/Entity Type

Home Builder

Number of Pages Required

5+ page

Font styles to use
Sans Serif

Requirements
Must have
• home page, about us page, gallery/portfolio page-showing various pictures of our work and different styles, services page and contact us.
• Use logo and similar colours as in logo for the scheme
• more content and pictures to follow...

```html
<!DOCTYPE html>
<html lang="en">
<head>
<meta charset="utf-8">
<title>Benvoe Cabinets – Home</title>
<link rel="stylesheet" href="https://fonts.googleapis.com/css2?family=Raleway:wght@400;500;600&family=Open+Sans:wght@400;600;700&display=swap">
<style>
  :root {
    --blue: #1e63b0;
    --orange: #f0680d;
    --ink: #222222;
    --body-text: #333333;
    --light-bg: #eeeeee;
    --white: #ffffff;
  }
  * { margin: 0; padding: 0; box-sizing: border-box; }
  html, body { width: 843px; height: 1200px; overflow: hidden; }
  body {
    position: relative;
    background: var(--white);
    font-family: "Open Sans", sans-serif;
    color: var(--body-text);
  }

  /* Header */
  .site-header { position: absolute; top: 0; left: 0; width: 843px; height: 85px; }
  .brand {
    position: absolute; left: 64px; top: 22px;
    display: flex; align-items: center; gap: 10px;
  }
  .brand-square { width: 34px; height: 34px; background: var(--blue); }
  .brand-name {
    font-family: "Raleway", sans-serif; font-weight: 600;
    font-size: 27px; color: var(--blue); letter-spacing: 0.5px;
  }
  .contact-info {
    position: absolute; right: 69px; top: 17px;
    font-size: 16px; color: var(--ink); text-align: right;
  }
  .contact-line { display: flex; align-items: center; justify-content: flex-end; gap: 8px; height: 26px; }
  .contact-line + .contact-line { margin-top: 3px; }
  .contact-line svg { width: 17px; height: 17px; fill: var(--ink); }

  /* Navigation */
  .main-nav {
    position: absolute; top: 85px; left: 0; width: 843px; height: 33px;
    background: var(--blue);
  }
  .main-nav a {
    position: absolute; top: 0; height: 33px; line-height: 33px;
    font-family: "Raleway", sans-serif; font-size: 14.5px; color: var(--white);
    text-decoration: none;
  }
  .main-nav .is-active { background: var(--orange); left: 54px; width: 88px; text-align: center; }

  /* Hero slider: bright white kitchen, grey island, dark timber floor */
  .hero {
    position: absolute; top: 126px; left: 0; width: 843px; height: 400px;
    background:
      radial-gradient(ellipse 260px 120px at 440px 195px, rgba(255,255,255,0.75), rgba(255,255,255,0) 70%),
      linear-gradient(90deg, rgba(235,236,236,0.9) 0%, rgba(235,236,236,0) 28%, rgba(0,0,0,0) 72%, rgba(215,217,218,0.6) 100%),
      linear-gradient(180deg,
        #d9dbdc 0%, #eceded 18%, #bfc2c2 40%,
        #f1f1f0 50%, #9a9ea2 58%, #7f8387 72%,
        #4b4442 86%, #2e2725 100%);
  }
  .slider-dots { position: absolute; top: 369px; left: 387px; display: flex; gap: 7.5px; }
  .slider-dots span { width: 11px; height: 11px; border-radius: 50%; background: var(--white); }
  .slider-dots .is-current { background: var(--orange); }

  /* Welcome */
  .welcome {
    position: absolute; top: 526px; left: 0; width: 843px; height: 198px;
    background: var(--light-bg); text-align: center;
  }
  .welcome h1 {
    margin-top: 27px; font-family: "Raleway", sans-serif; font-weight: 400;
    font-size: 29px; color: var(--blue); line-height: 36px;
  }
  .welcome h1 .accent { color: var(--orange); }
  .welcome p {
    width: 630px; margin: 0 auto; font-size: 10.3px; line-height: 16px; color: var(--body-text);
  }
  .welcome p:first-of-type { margin-top: 13px; }
  .welcome p + p { margin-top: 16px; }

  /* Feature grid */
  .tile { position: absolute; width: 421.5px; height: 197.5px; }
  /* traditional cream kitchen, dark mosaic splashback, dark stools */
  .tile-photo-a {
    top: 724px; left: 0;
    background:
      radial-gradient(ellipse 70px 60px at 140px 60px, rgba(70,72,78,0.75), rgba(70,72,78,0) 80%),
      radial-gradient(ellipse 80px 40px at 330px 80px, rgba(60,48,40,0.6), rgba(60,48,40,0) 80%),
      linear-gradient(180deg,
        #d6d3cc 0%, #c9c5bd 30%, #b8b3aa 48%,
        #e4dccd 62%, #cfc5b4 72%, #5a4c44 88%, #3b302b 100%);
  }
  /* white shaker kitchen, black worktops, warm timber floor */
  .tile-photo-b {
    top: 921.5px; left: 421.5px;
    background:
      radial-gradient(ellipse 90px 120px at 330px 70px, rgba(150,120,90,0.55), rgba(150,120,90,0) 80%),
      linear-gradient(180deg,
        #ece8e0 0%, #dcd6cc 35%, #2c2724 45%, #3a322d 50%,
        #e3ddd2 56%, #cfc6b8 72%, #7a5440 86%, #4a3024 100%);
  }
  .panel { text-align: center; color: var(--white); }
  .panel-blue { top: 724px; left: 421.5px; background: var(--blue); }
  .panel-orange { top: 921.5px; left: 0; background: var(--orange); }
  .panel h2 {
    margin-top: 17px; font-family: "Raleway", sans-serif; font-weight: 400;
    font-size: 29px; line-height: 36px;
  }
  .panel p { width: 320px; margin: 11px auto 0; font-size: 10.3px; line-height: 16px; }
  .btn-outline {
    display: inline-block; margin-top: 13px; padding: 0 14px; height: 34px; line-height: 31px;
    border: 1.5px solid var(--white); color: var(--white); text-decoration: none;
    font-family: "Raleway", sans-serif; font-weight: 600; font-size: 12px;
  }

  /* Footer */
  .site-footer {
    position: absolute; top: 1119px; left: 0; width: 843px; height: 81px;
    background: var(--blue); color: var(--white); text-align: center;
  }
  .footer-nav { display: flex; justify-content: center; margin-top: 18px; }
  .footer-nav a {
    font-family: "Raleway", sans-serif; font-size: 13px; color: var(--white);
    text-decoration: none; margin: 0 24px;
  }
  .copyright { margin-top: 10px; font-size: 11px; }
  .copyright strong { font-weight: 700; }
</style>
</head>
<body>

<header class="site-header">
  <div class="brand">
    <span class="brand-square"></span>
    <span class="brand-name">Benvoe Cabinets</span>
  </div>
  <div class="contact-info">
    <div class="contact-line">
      <svg viewBox="0 0 24 24" aria-hidden="true"><path d="M6.6 10.8a15.1 15.1 0 0 0 6.6 6.6l2.2-2.2c.3-.3.7-.4 1-.2 1.1.4 2.3.6 3.6.6.6 0 1 .4 1 1V20c0 .6-.4 1-1 1A17 17 0 0 1 3 4c0-.6.4-1 1-1h3.5c.6 0 1 .4 1 1 0 1.3.2 2.5.6 3.6.1.3 0 .7-.2 1z"/></svg>
      <span>123 456 789</span>
    </div>
    <div class="contact-line">
      <svg viewBox="0 0 24 24" aria-hidden="true"><path d="M2 5h20v2l-10 6L2 7z M2 9l10 6 10-6v10H2z"/></svg>
      <span>info@benvoecabinets.com</span>
    </div>
  </div>
</header>

<nav class="main-nav">
  <a class="is-active" href="#">Home</a>
  <a href="#" style="left:166px">About</a>
  <a href="#" style="left:256px">Gallery</a>
  <a href="#" style="left:354px">Services</a>
  <a href="#" style="left:459px">Contact</a>
</nav>

<section class="hero" role="img" aria-label="Bright white kitchen with grey island, quartz worktop, white bar stools and dark timber floor">
  <div class="slider-dots">
    <span class="is-current"></span><span></span><span></span><span></span>
  </div>
</section>

<section class="welcome">
  <h1>WELCOME TO <span class="accent">BENVOE CABINET</span></h1>
  <p>Lorem Ipsum is simply dummy text of the printing and typesetting industry. Lorem Ipsum has been the industry's standard dummy text ever since the 1500s, when an unknown printer took a galley of type and scrambled it to make a type specimen book. It has survived not only five centuries, but also the leap into electronic typesetting.</p>
  <p>Lorem Ipsum is simply dummy text of the printing and typesetting industry. Lorem Ipsum has been the industry's standard dummy text ever since the 1500s, when an unknown printer took...</p>
</section>

<div class="tile tile-photo-a" role="img" aria-label="Traditional cream kitchen with range hood, mosaic splashback, island and dark stools"></div>

<section class="tile panel panel-blue">
  <h2>Our Past Work</h2>
  <p>Lorem Ipsum is simply dummy text of the printing and typesetting industry. Lorem Ipsum has been the industry's standard dummy text ever since the 1500s, when an unknown printer took a galley of type and scrambled it to make a type specimen book.</p>
  <a class="btn-outline" href="#">READ MORE</a>
</section>

<section class="tile panel panel-orange">
  <h2>Our Services</h2>
  <p>Lorem Ipsum is simply dummy text of the printing and typesetting industry. Lorem Ipsum has been the industry's standard dummy text ever since the 1500s, when an unknown printer took a galley of type and scrambled it to make a type specimen book.</p>
  <a class="btn-outline" href="#">READ MORE</a>
</section>

<div class="tile tile-photo-b" role="img" aria-label="White shaker kitchen with black worktops and warm timber floor"></div>

<footer class="site-footer">
  <nav class="footer-nav">
    <a href="#">Home</a>
    <a href="#">About</a>
    <a href="#">Gallery</a>
    <a href="#">Services</a>
    <a href="#">Contact</a>
  </nav>
  <p class="copyright">© <strong>BENVOE CABINET</strong> - 2015. All Rights Reserved.</p>
</footer>

</body>
</html>
```